RM Tomás Rivera (Business Card)

Hi designers, in this work, I'm looking for an sophisticated stylish, elegant and proffesional personal card. We have a laboratory of pathology automated, with equipments high quality.
In this web the designers, have created my business logo, the name is "RM Tomás Rivera"
In our lab, we principal work is to prepare the biopsies for further diagnostic of diseases like cancer, tumors, etc.
I need that the first face, only having my complete logo (Rm Tomás Rivera, Laboratorio de procesamiento Histologico)
The overleaf, could repeat the same logo, like water logo.
In this face, I need to say: My full data:

Técnico en Anatomía Patológica
Tomás Rivera Ibarra M.P 47203
Av. Paredes Luján 418 - 2do piso - Instituto Marbel.
Córdoba, Argentina
(0351) 154820937
rivera.tomas@correolab.example

with respect the colors of card, use your imagination, the original logo color is violet, I haven't chosen a color base for the card.

attached pictures are examples of cards I like your DESIGN.
Attached too, the original logo to my company.

the size of card are:
horizontal: 9cm
vertical: 5,5cm

any question that you have, not doubt to question me,
Hand to work!

Industry/Entity Type

Laboratory

Requirements
Must have
• designers sophisticated, not simples, like show the images attached

```html
<!DOCTYPE html>
<html lang="es">
<head>
<meta charset="utf-8">
<title>Tomás Rivera – Tarjeta personal</title>
<link href="https://fonts.googleapis.com/css2?family=Open+Sans:wght@300;400;600;700&display=swap" rel="stylesheet">
<style>
  :root{
    --stage:#1a1a1c;
    --violet-deep:#3d1259;
    --violet:#5e2388;
    --violet-mid:#7a3aa6;
    --violet-soft:#b18fd0;
    --lavender:#d9c6ec;
    --white:#ffffff;
    --ink-grey:#6b6b70;
  }
  *{box-sizing:border-box;margin:0;padding:0}
  html,body{width:1200px;height:1130px;overflow:hidden}
  body{
    background:var(--stage);
    font-family:"Open Sans",Arial,sans-serif;
    display:flex;flex-direction:column;align-items:center;justify-content:center;gap:36px;
  }
  .card{
    position:relative;width:840px;height:513px;border-radius:22px;overflow:hidden;
  }
  /* Reverse side */
  .card--reverse{
    background:radial-gradient(ellipse at 40% 35%,var(--violet-mid) 0%,var(--violet) 45%,var(--violet-deep) 100%);
    display:flex;align-items:center;justify-content:center;
  }
  .title-mark{
    color:rgba(255,255,255,.42);font-weight:300;line-height:.95;letter-spacing:1px;
    display:grid;grid-template-columns:auto auto;column-gap:8px;
  }
  .title-mark__technician{grid-column:1/3;font-size:38px}
  .title-mark__in{font-size:38px;align-self:end}
  .title-mark__anatomy{font-size:78px;font-weight:400}
  .title-mark__pathology{grid-column:2;font-size:46px;text-align:right;padding-right:10px}

  /* Front side */
  .card--front{background:var(--white)}
  .card__waves{position:absolute;inset:0}
  .brand{
    position:absolute;left:40px;top:44px;display:flex;flex-direction:column;gap:10px;
  }
  .brand__row{display:flex;align-items:center;gap:14px}
  .brand__dot{width:44px;height:44px;border-radius:50%;background:var(--violet)}
  .brand__name{font-size:34px;font-weight:400;color:var(--violet);letter-spacing:2px}
  .brand__tagline{
    font-size:17px;font-weight:700;color:var(--ink-grey);letter-spacing:.5px;
    border-top:1px solid var(--ink-grey);padding-top:6px;
  }
  .holder{
    position:absolute;left:40px;top:300px;color:var(--lavender);font-size:22px;line-height:1.28;font-weight:400;
  }
  .holder__name{font-weight:400}
  .holder__reg{display:flex;align-items:center;gap:10px;color:var(--white)}
  .holder__reg-icon{
    width:22px;height:22px;border-radius:50%;background:var(--lavender);color:var(--violet);
    font-size:12px;font-weight:700;display:flex;align-items:center;justify-content:center;
  }
  .contact{
    position:absolute;left:430px;top:318px;color:var(--white);font-size:21px;line-height:1.27;
    list-style:none;
  }
  .contact li{display:flex;gap:10px;align-items:flex-start}
  .contact svg{width:18px;height:22px;flex:none;margin-top:3px;fill:var(--lavender)}
  .contact .contact__plain{padding-left:28px}
</style>
</head>
<body>

<section class="card card--reverse" aria-label="Reverso de la tarjeta">
  <div class="title-mark">
    <span class="title-mark__technician">TÉCNICO</span>
    <span class="title-mark__in">EN</span>
    <span class="title-mark__anatomy">ANATOMÍA</span>
    <span class="title-mark__pathology">PATOLÓGICA</span>
  </div>
</section>

<section class="card card--front" aria-label="Frente de la tarjeta">
  <svg class="card__waves" viewBox="0 0 840 513" preserveAspectRatio="none" aria-hidden="true">
    <defs>
      <linearGradient id="band" x1="0" y1="0" x2="1" y2="0">
        <stop offset="0" stop-color="#8a55b5"/>
        <stop offset="1" stop-color="#d8c4ea"/>
      </linearGradient>
      <linearGradient id="body" x1="0" y1="0" x2="1" y2="1">
        <stop offset="0" stop-color="#6c2c99"/>
        <stop offset="1" stop-color="#4e1a78"/>
      </linearGradient>
    </defs>
    <path d="M0,130 C210,95 360,230 580,236 C710,240 790,220 840,208 L840,513 L0,513 Z" fill="url(#band)"/>
    <path d="M0,165 C230,140 380,285 610,290 C730,292 800,276 840,266 L840,513 L0,513 Z" fill="url(#body)"/>
    <path d="M0,205 C240,190 420,310 640,318 C740,322 800,310 840,302" fill="none" stroke="#8f5cbc" stroke-width="2" opacity=".6"/>
  </svg>

  <header class="brand">
    <div class="brand__row">
      <span class="brand__dot"></span>
      <span class="brand__name">RM Tomás Rivera</span>
    </div>
    <span class="brand__tagline">LABORATORIO DE PROCESAMIENTO HISTOLOGICO</span>
  </header>

  <div class="holder">
    <p class="holder__name">Tomás Rivera Ibarra</p>
    <p>Técnico en Anatomía Patológica</p>
    <p class="holder__reg"><span class="holder__reg-icon">R</span>M.P 47203</p>
  </div>

  <ul class="contact">
    <li>
      <svg viewBox="0 0 18 22"><path d="M9 0a8 8 0 0 0-8 8c0 6 8 14 8 14s8-8 8-14a8 8 0 0 0-8-8zm0 11a3 3 0 1 1 0-6 3 3 0 0 1 0 6z"/></svg>
      <span>Av. Paredes Luján 418 - 2do piso</span>
    </li>
    <li class="contact__plain">Instituto Marbel.</li>
    <li class="contact__plain">Córdoba, Argentina</li>
    <li>
      <svg viewBox="0 0 18 22"><path d="M4 0h10a2 2 0 0 1 2 2v18a2 2 0 0 1-2 2H4a2 2 0 0 1-2-2V2a2 2 0 0 1 2-2zm0 3v14h10V3z"/></svg>
      <span>(0351) 154820937</span>
    </li>
    <li>
      <svg viewBox="0 0 18 22"><path d="M0 6h18v11H0zm2 2v1l7 4 7-4V8l-7 4z"/></svg>
      <span>rivera.tomas@correolab.example</span>
    </li>
  </ul>
</section>

</body>
</html>
```